Candle Label design

We would like to see different CREATIVE designs for three different collections of candles: - Celtic design, colour of the wax inside is always beige - design of the label distinguishes different candles smell (see picture for top design)- Metalic - wood design, wax is different colours see picture- Gel Candles - gels are different coloursWe would like to see designs for Celtic collections very different from metallic and gel candles - which can be in harmony with each other.The design should include design: lavender, fresh cotton and and roses

Target Market(s)

Candle lovers

Requirements
Must have
• Ideas for different smells of candle
• elegant
• Name of the candle
• place for weight (example 210g)
• designated position of logo
Nice to have
• Creative idea of candle label - not standard
Should not have
• a lot of colours

```html
<!DOCTYPE html>
<html lang="en">
<head>
<meta charset="utf-8">
<title>Gel Candle Label</title>
<link rel="stylesheet" href="https://fonts.googleapis.com/css2?family=Josefin+Slab:wght@400;600&display=swap">
<style>
  :root {
    --backdrop: #eef0f2;
    --label-white: #ffffff;
    --frame-terracotta: #d9714a;
    --maroon: #6b1a1f;
    --gold: #d4bd2a;
    --leaf-olive: #d8c65a;
    --leaf-orange: #ec9a4c;
    --leaf-rust: #c4502f;
  }
  * { box-sizing: border-box; margin: 0; padding: 0; }
  html, body {
    width: 927px;
    height: 1200px;
    overflow: hidden;
    background: var(--backdrop);
  }
  .canvas {
    position: relative;
    width: 927px;
    height: 1200px;
  }
  .label {
    position: absolute;
    left: 38px;
    top: 80px;
    width: 850px;
    height: 1040px;
    background: var(--label-white);
    box-shadow: 0 2px 10px rgba(0, 0, 0, 0.08);
  }
  .label__frame {
    position: absolute;
    left: 50px;
    top: 50px;
    width: 741px;
    height: 940px;
    border: 5px solid var(--frame-terracotta);
  }
  .label__foliage {
    position: absolute;
    left: 106px;
    width: 644px;
    background: radial-gradient(ellipse at center,
      var(--leaf-rust) 0%,
      var(--leaf-orange) 30%,
      var(--leaf-olive) 62%,
      rgba(216, 198, 90, 0) 100%);
    opacity: 0.85;
  }
  .label__foliage--top { top: 88px; height: 146px; border-radius: 50% 50% 0 0 / 100% 100% 0 0; }
  .label__foliage--bottom { top: 788px; height: 177px; border-radius: 0 0 50% 50% / 0 0 100% 100%; }
  .label__band {
    position: absolute;
    left: 0;
    top: 234px;
    width: 850px;
    height: 554px;
    background: var(--label-white);
    box-shadow: 0 3px 8px rgba(0, 0, 0, 0.12), 0 -2px 6px rgba(0, 0, 0, 0.06);
  }
  .brand-mark {
    position: absolute;
    left: 50%;
    top: 288px;
    width: 70px;
    height: 70px;
    margin-left: -35px;
    border-radius: 50%;
    background: var(--gold);
  }
  .text-line {
    position: absolute;
    left: 0;
    width: 850px;
    text-align: center;
    white-space: nowrap;
    line-height: 1;
    font-family: "Josefin Slab", Georgia, serif;
  }
  .brand-name { top: 392px; font-size: 44px; color: var(--maroon); }
  .product-name { top: 478px; font-size: 128px; font-weight: 600; color: var(--gold); letter-spacing: -2px; }
  .divider {
    position: absolute;
    left: 94px;
    top: 592px;
    width: 658px;
    height: 2px;
    background: var(--maroon);
  }
  .fragrance { top: 600px; font-size: 84px; color: var(--maroon); }
  .weight { top: 733px; font-size: 40px; color: var(--maroon); }
</style>
</head>
<body>
  <div class="canvas">
    <div class="label">
      <div class="label__frame"></div>
      <div class="label__foliage label__foliage--top" role="img" aria-label="Cluster of autumn leaves in olive, orange and rust"></div>
      <div class="label__foliage label__foliage--bottom" role="img" aria-label="Cluster of autumn leaves in olive, orange and rust"></div>
      <div class="label__band"></div>
      <div class="brand-mark"></div>
      <p class="text-line brand-name">Your Brand Name</p>
      <h1 class="text-line product-name">GEL CANDLE</h1>
      <div class="divider"></div>
      <p class="text-line fragrance">• Natural Fragrance •</p>
      <p class="text-line weight">210 Gr</p>
    </div>
  </div>
</body>
</html>
```